HAIR EXTENSIONS

We need a web design for a company base in Chicago called Extensions by Corvina. We sale 100% human hair in Brazilian body wave deep wave straight or natural curl, Peruvian body wave straight or deep wave. Malaysian loose straight or body wave, in the chicago land.
We also ship hair to any city or country. We like to see design that use the colors pinks & grays, or would just like to see some design creative with colors thats inviting.

Also I'm using the tamsworth template, Home- banner contact us, about us, Features- product side/left sidebar, Shop- wish list /shopping cart/ tracking your order / checkout/ order received.
Porfolio-filterable 4column portfolio
Blog. Buy now

Industry/Entity Type

Hair

Number of Pages Required

4 page

Colors
aaaaaa
606060
dddddd
eea4c8
d3a5cc
b868aa
a6459a
ffc213
1b1b1b

Requirements
Must have
• I NEED THE DESIGNER TO DO THE 4 PAGE LIKE THIS.
• 1.HOME-PAGE BANNER CONTACT US SOME PRODUCT WITH SIDING IMAGES OF THE TOP PROUDCT
• 2.PRODUCT WITH SHOPPING CART- I WANT SIDING BARS FOR PRODUCT & SHOPPING CART WITH TRACKING YOUR ORDERS CHECK OUT & ORDER RECEIVED.
• 3.PORFOLIO PHOTO-I WANT A FEATURES FOR CUSTOMERS TO UPLOAN THERE PICTURE & BLOG ON THE PAGE
• 4.ABOUT US- TALK ABOUT ARE COMPAMY.
Nice to have
• hello designer
• I was working with a web developer for my site be for i came to pixelforgly & they build a site for me that i liked, You all can view it at www.Extensionsbycorvina.info
• long story short never could get them to finish the project after they got paid!!
• I know, why paid before its finish bad decision. So know I'm here starting over with you all.
• here is a list of my competition site
• www.tressvaultly.com
• www.lokawaves.com
• www.pellitashoppe.com
• So just to give some insight, I'm looking for something like the one i had builded.

```html
<!DOCTYPE html>
<html lang="en">
<head>
<meta charset="utf-8">
<title>Hair Extensions — Extensions by Corvina</title>
<link rel="stylesheet" href="https://fonts.googleapis.com/css2?family=Open+Sans:wght@300;400;600;700&family=Raleway:wght@400;500;700;800&display=swap">
<style>
:root{
  --pink:#e6127f;
  --pink-soft:#eea4c8;
  --ink:#1b1b1b;
  --dark:#2a2a2a;
  --grey:#606060;
  --grey-mid:#aaaaaa;
  --grey-light:#dddddd;
  --paper:#ffffff;
  --hero-bg:#ececec;
}
*{box-sizing:border-box;margin:0;padding:0}
html,body{width:783px;height:1200px;overflow:hidden}
body{font-family:"Open Sans",Arial,sans-serif;color:var(--ink);background:var(--paper);position:relative}
a{color:inherit;text-decoration:none}

/* header */
.site-header{position:absolute;left:0;top:0;width:783px;height:100px;background:linear-gradient(#1e1e1e,#2c2c2c)}
.call-line{position:absolute;left:63px;top:8px;font-size:11px;color:#ddd;display:flex;align-items:center;gap:6px}
.call-line .label{color:var(--pink);font-weight:600}
.call-line .num{font-size:13px;font-weight:600;color:#fff}
.brand{position:absolute;left:63px;top:34px;font-family:"Open Sans",sans-serif;font-weight:300;font-size:40px;color:#fff;letter-spacing:.5px;line-height:1}
.social{position:absolute;right:62px;top:8px;display:flex;gap:5px}
.social span{width:15px;height:15px;border-radius:50%;background:#fff;display:block}
.account-links{position:absolute;right:62px;top:40px;font-size:9px;color:#eee;display:flex;gap:16px}
.cart-box{position:absolute;right:62px;top:63px;display:flex;align-items:center;gap:8px}
.cart-box .icon{width:26px;height:22px;background:var(--grey-mid);border-radius:3px}
.cart-box .txt{font-size:8px;color:#ccc;line-height:1.3}
.cart-box .txt b{color:var(--pink);font-weight:600}

/* nav */
.main-nav{position:absolute;left:0;top:100px;width:783px;height:32px;background:var(--paper);border-bottom:1px solid var(--grey-light)}
.main-nav ul{list-style:none;position:absolute;left:63px;top:0;display:flex;height:32px}
.main-nav li{font-size:11px;font-weight:600;color:#333;padding:0 22px;display:flex;align-items:center;border-right:1px solid var(--grey-light);position:relative}
.main-nav li:first-child{padding-left:8px}
.main-nav li.active::after{content:"";position:absolute;left:0;right:0;bottom:0;height:3px;background:var(--pink)}
.search{position:absolute;right:62px;top:6px;width:190px;height:20px;border-bottom:1px solid var(--grey-light);font-size:9px;color:var(--grey);padding:4px 6px}
.search svg{position:absolute;right:2px;top:3px}

/* hero */
.hero{position:absolute;left:0;top:132px;width:783px;height:363px;background:linear-gradient(90deg,#d9d9d9 0%,#f1f1f1 45%,#ececec 100%)}
.hero-photo{position:absolute;left:63px;top:0;width:300px;height:363px;background:radial-gradient(ellipse at 55% 45%,#caa08f 0%,#7b5245 30%,#2b1b17 60%,rgba(40,26,22,0) 85%)}
.hero-copy{position:absolute;left:380px;top:100px;width:340px}
.hero-copy h1{font-family:"Raleway",sans-serif;font-weight:500;font-size:27px;color:#333;line-height:1.15}
.hero-copy h2{font-family:"Raleway",sans-serif;font-weight:800;font-size:32px;color:var(--pink);line-height:1.2;margin-top:2px}
.hero-copy p{font-size:9.5px;color:var(--grey);line-height:1.5;margin-top:8px;width:320px}
.btn-shop{position:absolute;right:0;top:160px;background:var(--pink);color:#fff;font-family:"Raleway",sans-serif;font-weight:700;font-size:15px;padding:8px 14px}

/* featured */
.featured{position:absolute;left:63px;top:525px;width:657px}
.featured h3{font-family:"Raleway",sans-serif;font-weight:700;font-size:17px;color:#222}
.featured .rule{height:1px;background:var(--grey-light);margin-top:8px;position:relative}
.featured .rule::before{content:"";position:absolute;left:0;top:-1px;width:60px;height:3px;background:var(--pink)}
.arrows{position:absolute;right:0;top:2px;display:flex;gap:4px}
.arrows span{width:16px;height:16px;border:1px solid #555;display:flex;align-items:center;justify-content:center}
.products{display:flex;gap:19px;margin-top:16px}
.card{width:150px;text-align:center;position:relative}
.card .photo{height:212px;position:relative;overflow:hidden}
.p1{background:linear-gradient(160deg,#e8d7cf,#6b4a3a 55%,#d9c7bd)}
.p2{background:linear-gradient(160deg,#efe6e0,#4a3128 50%,#e2d4cb)}
.p3{background:linear-gradient(160deg,#f0e2cc,#c9965d 45%,#d9536f 70%,#efe4d6)}
.p4{background:linear-gradient(160deg,#f2e8de,#a9794b 50%,#ebdbc8)}
.card .badge{position:absolute;right:0;top:0;width:0;height:0;border-top:34px solid var(--pink);border-left:34px solid transparent}
.card .tools{position:absolute;left:0;right:0;bottom:20px;display:flex;justify-content:center;gap:5px}
.card .tools span{width:14px;height:14px;border-radius:50%;background:#fff}
.card .add{position:absolute;left:0;right:0;bottom:0;height:20px;background:var(--pink);color:#fff;font-size:10px;font-weight:700;line-height:20px;letter-spacing:.3px}
.card .name{font-size:10px;color:#333;margin-top:7px}
.card .price{font-size:10px;margin-top:3px}
.card .price b{color:var(--pink);font-weight:700}
.card .price s{color:var(--grey-mid);font-size:9px;margin-left:4px}

/* contact */
.contact{position:absolute;left:0;top:843px;width:783px;height:292px;background:linear-gradient(90deg,#3a3a3a 0%,#4a4a4a 40%,#6e6e6e 75%,#8a8a8a 100%)}
.contact::after{content:"";position:absolute;inset:0;background:rgba(20,20,20,.35)}
.contact-inner{position:relative;z-index:1}
.contact h3{position:absolute;left:0;width:783px;top:20px;text-align:center;font-family:"Raleway",sans-serif;font-weight:800;font-size:32px;color:#fff;letter-spacing:1px}
.form{position:absolute;left:63px;top:92px;width:282px}
.field{background:#fff;height:26px;margin-bottom:10px;font-size:9px;color:var(--grey);padding:7px 9px}
.field.msg{height:104px}
.btn-send{position:absolute;left:348px;top:252px;width:64px;height:24px;background:var(--pink);color:#fff;font-family:"Raleway",sans-serif;font-weight:700;font-size:14px;text-align:center;line-height:24px}
.info{position:absolute;left:400px;top:94px;color:#fff}
.info h4{font-family:"Raleway",sans-serif;font-weight:500;font-size:18px;letter-spacing:.5px}
.info .row{display:flex;align-items:center;gap:10px;font-size:12px;margin-top:16px}
.info .row .ico{width:16px;height:16px;display:flex;align-items:center;justify-content:center}
.info .squares{display:flex;gap:5px;margin-top:14px}
.info .squares span{width:14px;height:14px;background:#ddd}

/* footer */
.site-footer{position:absolute;left:0;top:1135px;width:783px;height:65px;background:var(--grey-light)}
.foot-links{position:absolute;left:63px;top:14px;font-size:9px;color:#333;display:flex;gap:10px}
.foot-links span.sep{color:var(--grey-mid)}
.copyright{position:absolute;left:63px;top:34px;font-size:8.5px;color:var(--grey)}
.pay-badge{position:absolute;right:62px;top:10px;width:70px;height:40px;background:#f4f4f4;border:1px solid var(--grey-mid);border-radius:4px}
</style>
</head>
<body>

<header class="site-header">
  <div class="call-line">
    <svg width="11" height="11" viewBox="0 0 24 24"><path fill="#e6127f" d="M6.6 10.8a15 15 0 006.6 6.6l2.2-2.2c.3-.3.7-.4 1-.2 1.1.4 2.3.6 3.6.6.6 0 1 .4 1 1V20c0 .6-.4 1-1 1A17 17 0 013 4c0-.6.4-1 1-1h3.5c.6 0 1 .4 1 1 0 1.3.2 2.5.6 3.6.1.3 0 .7-.2 1z"/></svg>
    <span class="label">Call 24/7 Hours:</span><span class="num">865 555-0142</span>
  </div>
  <div class="brand">Hair Extensions</div>
  <div class="social"><span></span><span></span><span></span><span></span><span></span></div>
  <nav class="account-links"><a>Order Received</a><a>My Account</a><a>Checkout</a></nav>
  <div class="cart-box">
    <span class="icon"></span>
    <div class="txt"><b>Shopping Cart</b><br>Items in your cart $0.00</div>
  </div>
</header>

<nav class="main-nav">
  <ul>
    <li class="active">Home</li>
    <li>banner</li>
    <li>contact us</li>
    <li>about us</li>
  </ul>
  <div class="search">tracking your order
    <svg width="12" height="12" viewBox="0 0 24 24"><circle cx="10" cy="10" r="7" fill="none" stroke="#333" stroke-width="2.5"/><line x1="15" y1="15" x2="22" y2="22" stroke="#333" stroke-width="2.5"/></svg>
  </div>
</nav>

<section class="hero">
  <div class="hero-photo" role="img" aria-label="Woman with long dark curly hair"></div>
  <div class="hero-copy">
    <h1>Get The Long Hair You've</h1>
    <h2>Never Had Before!</h2>
    <p>Lorem ipsum dolor sit amet, consectetur adipiscing elit. Sed do eiusmod tempor incididunt ut labore et dolore magna aliqua.</p>
    <a class="btn-shop">Shop Now</a>
  </div>
</section>

<section class="featured">
  <h3>Featured Product</h3>
  <div class="arrows">
    <span><svg width="6" height="8" viewBox="0 0 6 8"><path d="M5 0L1 4l4 4" fill="none" stroke="#333" stroke-width="1.5"/></svg></span>
    <span><svg width="6" height="8" viewBox="0 0 6 8"><path d="M1 0l4 4-4 4" fill="none" stroke="#333" stroke-width="1.5"/></svg></span>
  </div>
  <div class="rule"></div>
  <div class="products">
    <div class="card">
      <div class="photo p1" role="img" aria-label="Model with long dark wavy hair extensions">
        <span class="badge"></span>
        <div class="tools"><span></span><span></span><span></span></div>
        <div class="add">ADD TO CART</div>
      </div>
      <div class="name">Lorem Ipsum is</div>
      <div class="price"><b>$1170.46</b><s>$1170.46</s></div>
    </div>
    <div class="card">
      <div class="photo p2" role="img" aria-label="Model with long straight dark brown hair"></div>
      <div class="name">Lorem Ipsum is</div>
      <div class="price"><b>$1170.46</b><s>$1170.46</s></div>
    </div>
    <div class="card">
      <div class="photo p3" role="img" aria-label="Model with blonde hair and pink streaks"></div>
      <div class="name">Lorem Ipsum is</div>
      <div class="price"><b>$1170.46</b><s>$1170.46</s></div>
    </div>
    <div class="card">
      <div class="photo p4" role="img" aria-label="Model with long light brown wavy hair"></div>
      <div class="name">Lorem Ipsum is</div>
      <div class="price"><b>$1170.46</b><s>$1170.46</s></div>
    </div>
  </div>
</section>

<section class="contact" role="img" aria-label="Hair stylist blow-drying a client's hair">
  <div class="contact-inner">
    <h3>CONTACT</h3>
    <div class="form">
      <div class="field">Full Name</div>
      <div class="field">Email</div>
      <div class="field msg">Message</div>
    </div>
    <a class="btn-send">SEND</a>
    <div class="info">
      <h4>CONTACT INFO</h4>
      <div class="row"><span class="ico"><svg width="14" height="14" viewBox="0 0 24 24"><path fill="#e6127f" d="M6.6 10.8a15 15 0 006.6 6.6l2.2-2.2c.3-.3.7-.4 1-.2 1.1.4 2.3.6 3.6.6.6 0 1 .4 1 1V20c0 .6-.4 1-1 1A17 17 0 013 4c0-.6.4-1 1-1h3.5c.6 0 1 .4 1 1 0 1.3.2 2.5.6 3.6.1.3 0 .7-.2 1z"/></svg></span>8755550186</div>
      <div class="row"><span class="ico"><svg width="16" height="12" viewBox="0 0 16 12"><rect width="16" height="12" rx="1.5" fill="#e6127f"/><path d="M1 1l7 6 7-6" fill="none" stroke="#fff" stroke-width="1.2"/></svg></span>info@corvinahair.com</div>
      <div class="squares"><span></span><span></span></div>
    </div>
  </div>
</section>

<footer class="site-footer">
  <div class="foot-links"><a>Home</a><span class="sep">|</span><a>banner</a><span class="sep">|</span><a>contact us</a><span class="sep">|</span><a>about us</a></div>
  <div class="copyright">© 2014 Copyright Extensions by Corvina. All Rights Reserved.</div>
  <div class="pay-badge"></div>
</footer>

</body>
</html>
```